Design for a real estate wev portal

Contents and features of the site
---------------------------------
Website in 5 languages: French, Dutch, English, German, Spanish.
English name of the site: Lantern Nest Place
Main purpose of the site:
- allow people to rent their house/ appartment for flatsharing purposes.
- help people wanting to find a room in flatsharing
- help people to find additional roommates for their flatsharing
Key interaction sequence:
1. I create a "group" of people who have common interest/hobbies
2. People who have the same interests/hobbies join my group
3. I look for a house/appartment to host my group
Website structure will be the following:
- Home
- Groups
-- Look for a group
--- Join a group
-- Create a group
- Properties
-- Look for a house/appartement
-- Apply
- Sales conditions
- Contact
- My account
-- My profile
-- My groups OR my properties
Your mission
------------
The client has no graphical guidelines, simply a logo (see attached).
We need a (responsive compliant) design for the following pages (we expect PSD's from you. No HTML nor CSS):
1. homepage (see example and wireframe attached)
2. properties search result list (see wireframe attached)
3. "detailed" form for properties
4. groups search result list
5. "detailed" form for groups
6. my account page
FOR THE COMPETITION step we only expect from you the design of first 2 screens.
Based on that, we will select the designer who will win the project, and will have to design the 4 remaining screens.
Target Market(s)
B2C
Industry/Entity Type
Real Estate
Number of Pages Required
5+ page
Look and feel
Each slider illustrates characteristics of the customer's brand and the style your logo design should communicate.

```html
<!DOCTYPE html>
<html lang="en">
<head>
<meta charset="utf-8">
<title>Lantern Nest Place — Home</title>
<link href="https://fonts.googleapis.com/css2?family=Montserrat:wght@300;400;600;700&family=Lato:wght@400;700&display=swap" rel="stylesheet">
<style>
:root{
  --teal:#14a0b2;
  --teal-dark:#0f8d9e;
  --green:#6abf45;
  --green-dark:#5aad37;
  --ink:#333;
  --muted:#666;
  --dark:#3b3b3b;
  --light:#eeeeee;
  --white:#fff;
}
*{box-sizing:border-box;margin:0;padding:0}
html,body{width:1200px;height:2571px;overflow:hidden}
body{font-family:'Lato',sans-serif;color:var(--ink);background:var(--white);position:relative}
h1,h2,h3,h4,.btn,.nav a{font-family:'Montserrat',sans-serif}
a{color:inherit;text-decoration:none}

/* header */
.site-header{position:absolute;top:0;left:0;width:1200px;height:79px;background:var(--dark);z-index:10}
.brand{position:absolute;left:99px;top:0;width:184px;height:132px;background:var(--white);
  clip-path:polygon(0 0,100% 0,100% 100%,50% 88%,0 100%);display:flex;align-items:center;justify-content:center;gap:10px;padding-bottom:12px}
.brand-dot{width:14px;height:14px;border-radius:50%;background:var(--green);flex:none}
.brand-name{font-family:'Montserrat',sans-serif;font-weight:700;font-size:20px;color:var(--teal);line-height:1.1;white-space:nowrap}
.utility{position:absolute;right:99px;top:8px;display:flex;gap:22px;font-size:10px;color:#ddd;font-weight:700}
.nav{position:absolute;right:99px;top:34px;display:flex;gap:40px}
.nav a{color:#ddd;font-size:13px;font-weight:700;letter-spacing:.3px}
.nav a.active{color:var(--white)}

/* hero */
.hero{position:absolute;top:79px;left:0;width:1200px;height:487px;display:flex}
.hero-half{width:600px;height:100%;text-align:center;color:var(--white);padding-top:100px}
.hero-half.seekers{background:var(--teal);padding-left:99px;padding-right:26px}
.hero-half.owners{background:var(--green);padding-left:31px;padding-right:99px}
.hero-title{font-weight:300;font-size:34px;letter-spacing:1px;line-height:1}
.hero-title strong{display:flex;align-items:center;gap:14px;justify-content:center;font-weight:700;font-size:26px;margin-top:4px;white-space:nowrap}
.hero-title strong::before,.hero-title strong::after{content:"";flex:1;height:2px;background:var(--white)}
.hero-choices{display:flex;justify-content:space-between;margin-top:26px}
.choice{width:230px}
.choice-photo{width:212px;height:212px;border-radius:50%;margin:0 auto;border:7px solid rgba(255,255,255,.45)}
.choice p{font-family:'Montserrat',sans-serif;font-weight:700;font-size:15px;margin-top:16px;line-height:1.2}

/* section headings */
.section-heading{text-align:left;margin:0 auto;width:410px}
.section-heading h2{font-size:26px;font-weight:700;color:var(--ink);letter-spacing:.5px;line-height:1}
.section-heading span{display:block;font-family:'Montserrat',sans-serif;font-size:25px;font-weight:400;color:var(--ink);line-height:1.1}

/* spotlight */
.spotlight{position:absolute;top:566px;left:0;width:1200px;height:660px}
.spotlight .section-heading{position:absolute;top:115px;left:440px}
.card{position:absolute;width:487px;height:145px;display:flex}
.card-photo{width:146px;height:145px;position:relative;flex:none}
.card-body{flex:1;min-width:0;border:4px solid var(--teal);border-left:none;padding:24px 14px 0;position:relative;background:var(--white)}
.card.house .card-body{border-color:var(--green)}
.card h3{font-size:15px;font-weight:700;letter-spacing:.5px;color:var(--ink)}
.card p{font-size:12.5px;color:var(--muted);line-height:1.35;margin-top:2px}
.card .meta{font-size:10px;color:#444;margin-top:6px;display:flex;gap:10px;align-items:center}
.card.house .meta{margin-top:2px;margin-bottom:4px}
.card-actions{position:absolute;right:-4px;bottom:-4px;display:flex;gap:2px}
.card-actions span{width:24px;height:24px;display:flex;align-items:center;justify-content:center;background:var(--teal)}
.card-actions span.fav{background:#8fcdd6}
.card.house .card-actions span{background:var(--green)}
.card.house .card-actions span.fav{background:#a8d890}
.price{position:absolute;right:0;bottom:0;background:rgba(0,0,0,.55);color:var(--white);font-size:13px;padding:4px 8px}
.price small{font-size:9px}
.btn{position:absolute;display:flex;align-items:center;justify-content:center;width:184px;height:38px;border-radius:5px;color:var(--white);font-size:11.5px;font-weight:700;letter-spacing:.3px}
.btn.teal{background:var(--teal)}
.btn.green{background:var(--green)}
.btn.dark{background:var(--dark);width:184px;height:37px}

/* selling points */
.selling{position:absolute;top:1226px;left:0;width:1200px;height:402px}
.selling-band{height:77px;background:var(--light);display:flex;align-items:center;justify-content:center}
.selling-band h2{font-size:24px;font-weight:700;letter-spacing:.5px;color:var(--ink)}
.selling-panels{display:flex;height:325px;position:relative}
.selling-panels::after{content:"";position:absolute;left:572px;top:0;border:28px solid transparent;border-top:16px solid var(--light);border-bottom:none}
.panel{width:600px;padding:52px 26px 0 99px;color:var(--white)}
.panel.roommates{background:var(--teal)}
.panel.owners{background:var(--green);padding-left:28px;padding-right:99px}
.panel h3{font-size:20px;font-weight:700;letter-spacing:.5px;margin-bottom:8px}
.panel p{font-family:'Montserrat',sans-serif;font-weight:600;font-size:12.4px;line-height:1.55}

/* faq */
.faq{position:absolute;top:1628px;left:0;width:1200px;height:626px}
.faq .section-heading{position:absolute;top:116px;left:373px;width:500px}
.faq-item{position:absolute;left:99px;width:1002px;height:80px;display:flex;background:var(--light);padding:4px}
.faq-num{width:80px;flex:none;display:flex;align-items:center;justify-content:center;font-family:'Montserrat',sans-serif;font-weight:300;font-size:48px;color:#777}
.faq-text{flex:1;background:var(--white);padding:8px 12px;font-size:11.3px;line-height:1.5;color:#555}
.faq-text a{font-family:'Montserrat',sans-serif;font-weight:700;font-size:10px;color:var(--ink);text-decoration:underline}

/* filter footer */
.filters{position:absolute;top:2254px;left:0;width:1200px;height:126px;display:flex}
.filter-half{width:600px;display:flex;gap:14px;padding:22px 26px 0 99px;color:var(--white)}
.filter-half.seekers{background:var(--teal)}
.filter-half.owners{background:var(--green);padding-left:28px;padding-right:99px}
.filter-col{flex:1}
.filter-col h4{font-size:12.5px;font-weight:700;letter-spacing:.3px;padding-bottom:4px;border-bottom:1px solid rgba(255,255,255,.8);margin-bottom:7px}
.filter-col li{list-style:none;font-family:'Montserrat',sans-serif;font-size:10.5px;font-weight:600;line-height:1.7}
.filter-col li::before{content:"• "}

/* site footer */
.site-footer{position:absolute;top:2380px;left:0;width:1200px;height:191px;background:var(--dark);display:flex;gap:27px;padding:36px 99px 0;color:#ccc}
.foot-col{width:230px}
.foot-col h4{font-size:12.5px;font-weight:700;letter-spacing:.3px;color:#ddd;padding-bottom:4px;border-bottom:1px solid #777;margin-bottom:8px;position:relative}
.foot-col h4::after{content:"";position:absolute;right:0;bottom:-3px;width:5px;height:5px;border-radius:50%;background:#777}
.foot-col li{list-style:none;font-size:10.5px;line-height:1.72}
.foot-col li::before{content:"» "}
.contact-line{font-size:10.5px;line-height:1.72}
.social{display:flex;gap:5px;margin:4px 0 6px}
.social span{width:24px;height:24px;border-radius:50%;background:#bbb}
.copyright{font-size:10px}
</style>
</head>
<body>

<header class="site-header">
  <a class="brand" href="#"><span class="brand-dot"></span><span class="brand-name">Lantern Nest<br>Place</span></a>
  <div class="utility"><span>English ▾</span><span>● My Account ▾</span></div>
  <nav class="nav">
    <a class="active" href="#">HOME</a>
    <a href="#">GROUPS +</a>
    <a href="#">PROPERTIES +</a>
    <a href="#">SALES CONDITIONS</a>
    <a href="#">CONTACT</a>
  </nav>
</header>

<section class="hero">
  <div class="hero-half seekers">
    <h1 class="hero-title">SEARCHING<strong>FOR ACCOMMODATION</strong></h1>
    <div class="hero-choices">
      <div class="choice">
        <div class="choice-photo" role="img" aria-label="Young woman working on a laptop in a café" style="background:radial-gradient(circle at 45% 45%,#d9b88c,#8a6a4a)"></div>
        <p>I want to rent a room<br>right now!</p>
      </div>
      <div class="choice">
        <div class="choice-photo" role="img" aria-label="Smiling young man with a beard in a busy café" style="background:radial-gradient(circle at 50% 45%,#6fa0c0,#35506a)"></div>
        <p>I want to join a group!</p>
      </div>
    </div>
  </div>
  <div class="hero-half owners">
    <h1 class="hero-title">I HAVE A<strong>HOUSE FOR RENT</strong></h1>
    <div class="hero-choices">
      <div class="choice">
        <div class="choice-photo" role="img" aria-label="Small model house standing on a table" style="background:radial-gradient(circle at 50% 50%,#c9c9c4,#595c58)"></div>
        <p>I want to advertise!</p>
      </div>
      <div class="choice">
        <div class="choice-photo" role="img" aria-label="Group of flatmates cooking together in a kitchen" style="background:radial-gradient(circle at 50% 50%,#e6cfa8,#8c7458)"></div>
        <p>Why is flatsharing<br>interesting for me?</p>
      </div>
    </div>
  </div>
</section>

<section class="spotlight">
  <div class="section-heading"><h2>UNDER THE SPOTLIGHT</h2><span>You May Be Interested In</span></div>

  <article class="card group" style="left:99px;top:197px">
    <div class="card-photo" role="img" aria-label="Group of young friends laughing together" style="background:linear-gradient(135deg,#b58a62,#5b4636)"></div>
    <div class="card-body">
      <h3>A NICE GROUP</h3>
      <p>Young workers, seeking for accommodation<br>downtown.</p>
      <div class="meta"><span>Average age: 35 YO</span>|<span>Men &amp; Women welcome</span></div>
      <div class="card-actions"><span class="fav"><svg width="12" height="11" viewBox="0 0 12 11"><path d="M6 10.5 1 5.5A3 3 0 0 1 6 1.6 3 3 0 0 1 11 5.5Z" fill="#fff"/></svg></span><span><svg width="9" height="12" viewBox="0 0 9 12"><path d="M2 1l5 5-5 5" stroke="#fff" stroke-width="2.4" fill="none"/></svg></span></div>
    </div>
  </article>

  <article class="card group" style="left:99px;top:356px">
    <div class="card-photo" role="img" aria-label="Young women students smiling outdoors" style="background:linear-gradient(135deg,#9fc2d0,#4d6470)"></div>
    <div class="card-body">
      <h3>ANOTHER NICE GROUP</h3>
      <p>Young ladies, studying at University seeking for<br>accommodation close to Brussels University.</p>
      <div class="meta"><span>Average age: 20 YO</span>|<span>Women only</span></div>
      <div class="card-actions"><span class="fav"><svg width="12" height="11" viewBox="0 0 12 11"><path d="M6 10.5 1 5.5A3 3 0 0 1 6 1.6 3 3 0 0 1 11 5.5Z" fill="#fff"/></svg></span><span><svg width="9" height="12" viewBox="0 0 9 12"><path d="M2 1l5 5-5 5" stroke="#fff" stroke-width="2.4" fill="none"/></svg></span></div>
    </div>
  </article>

  <article class="card house" style="left:614px;top:197px">
    <div class="card-photo" role="img" aria-label="Detached house with a front lawn" style="background:linear-gradient(160deg,#a9c4dc,#6f7d66)"><span class="price">€350 <small>/mo</small></span></div>
    <div class="card-body">
      <h3>HOUSE: NAME</h3>
      <div class="meta"><span>⚲ Manchester</span><span>▣ Available Now</span></div>
      <p>Lorem ipsum dolor sit amet, consectetur adipiscing elit<br>vivamus destibulum ultricies enim ryeu ultricies.</p>
      <div class="card-actions"><span class="fav"><svg width="12" height="11" viewBox="0 0 12 11"><path d="M6 10.5 1 5.5A3 3 0 0 1 6 1.6 3 3 0 0 1 11 5.5Z" fill="#fff"/></svg></span><span><svg width="9" height="12" viewBox="0 0 9 12"><path d="M2 1l5 5-5 5" stroke="#fff" stroke-width="2.4" fill="none"/></svg></span></div>
    </div>
  </article>

  <article class="card house" style="left:614px;top:356px">
    <div class="card-photo" role="img" aria-label="Brick apartment building with front steps" style="background:linear-gradient(160deg,#b8733f,#5c3a22)"><span class="price">€480 <small>/mo</small></span></div>
    <div class="card-body">
      <h3>APT: NAME</h3>
      <div class="meta"><span>⚲ Paris</span><span>▣ Available from December, 2016</span></div>
      <p>Nam ultricies justo risus, id bibendum mauris<br>vestibulum dignissim. aenean ultrices lacus nuncpl.</p>
      <div class="card-actions"><span class="fav"><svg width="12" height="11" viewBox="0 0 12 11"><path d="M6 10.5 1 5.5A3 3 0 0 1 6 1.6 3 3 0 0 1 11 5.5Z" fill="#fff"/></svg></span><span><svg width="9" height="12" viewBox="0 0 9 12"><path d="M2 1l5 5-5 5" stroke="#fff" stroke-width="2.4" fill="none"/></svg></span></div>
    </div>
  </article>

  <a class="btn teal" href="#" style="left:403px;top:514px">SEE MORE GROUPS »</a>
  <a class="btn green" href="#" style="left:917px;top:514px">SEE MORE HOUSES »</a>
</section>

<section class="selling">
  <div class="selling-band"><h2>KEY SELLING POINT</h2></div>
  <div class="selling-panels">
    <div class="panel roommates">
      <h3>FOR THE ROOMMATES:</h3>
      <p>Lorem ipsum dolor sit amet, consectetur adipiscing elit. Duis luctus odio ornare lacus vehicula mollis. Ut quis tortor felis. Proin egestas sem vel purus sagittis, semper ullamcorper tellus euismod. Donec eget mi non lacus tempor pellentesque sed aliquam velit. Pellentesque in ipsum quis ligula commodo suscipit. Aenean at leo at est rutrum lacinia eu accumsan urna vestibulum. enim consequat sapien volutpat finibus. In diam nisi, imperdiet nec semper nec, gravida vitae est. Fusce volutpat orci neque, non placerat urna tincidunt vivamus ac consequat tellus, sed fermentum. erat. Suspendisse mattis mollis lectus. in finibus ligula pretium faucibus. Nam auctor, eros eu congue condimentum, turpis.</p>
    </div>
    <div class="panel owners">
      <h3>FOR THE OWNERS:</h3>
      <p>Morbi eget efficitur dolor. Cras eu dolor metus. Curabitur nisi dolor, vulputate eget ipsum id, tempor pellentesque nisl. Aliquam erat volutpat. Nulla eleifend euismod tellus, ac blandit neque suscipit et. Nulla sit amet bibendum nunc. Donec efficitur ligula sit amet arcu commodo tincidunt. Nulla quis nunc quis lacus viverra convallis. Aliquam ac arcu non mi convallis luctus a ac eros. Nullam congue velit orci, at egestas massa mollis sed. Interdum et malesuada fames ac ante ipsum primis in faucibus. Suspendisse auctor ante quis pellentesque finibus. Duis feugiat vulputate porttitor. Fusce placerat diam accumsan ex laoreet, iaculis commodo felis laoreet curabitur malesuada eleifend.</p>
    </div>
  </div>
</section>

<section class="faq">
  <div class="section-heading"><h2>EVERYTHING YOU NEED TO KNOW</h2><span>About Flatsharing</span></div>
  <div class="faq-item" style="top:198px">
    <div class="faq-num">1</div>
    <div class="faq-text">Sed id arcu est. Ut congue orci id fringilla vestibulum. Donec commodo porta ante, vel tristique lacus pellentesque a. Duis cursus tincidunt neque, nec feugiat velit ornare ut. Nam consectetur dapibus mauris, et vulputate nisl eleifend id. Proin id iaculis ex. Aliquam tristique bibendum libero, ac dapibus lorem varius vel. Aenean pellentesque sapien sit amet augue ultrices, ac pellentesque nulla consectetur. Curabitur ac ipsum finibus, sodales nunc nec, porttitor... <a href="#">MORE »</a></div>
  </div>
  <div class="faq-item" style="top:292px">
    <div class="faq-num">2</div>
    <div class="faq-text">Cras in ex eget tellus aliquet dignissim vel eget sapien. Mauris malesuada, lectus ac rhoncus accumsan, libero lacus dictum elit, non malesuada odio elit ac sapien. Maecenas aliquet mollis libero sit amet lobortis. Fusce nec egestas turpis. Mauris id arcu condimentum, scelerisque risus eget, porttitor lorem. Morbi maximus nulla sed lacus dictum faucibus eu vitae lorem. Donec elementum interdum accumsan. Vivamus lacus leo, semper vel posuere id, ultricies... <a href="#">MORE »</a></div>
  </div>
  <div class="faq-item" style="top:388px">
    <div class="faq-num">3</div>
    <div class="faq-text">Donec commodo porta ante, vel tristique lacus pellentesque a. Duis cursus tincidunt neque, nec feugiat velit ornare ut. Nam consectetur dapibus mauris, et vulputate nisl eleifend id. Proin id iaculis ex. Aliquam tristique bibendum libero, ac dapibus lorem varius vel. Aenean pellentesque sapien sit amet augue ultrices, ac pellentesque nulla consectetur. Curabitur ac ipsum finibus, sodales nunc nec, porttitor sapien. In volutpat urna sit amet nisi euismod... <a href="#">MORE »</a></div>
  </div>
  <a class="btn dark" href="#" style="left:508px;top:484px">ALL QUESTIONS »</a>
</section>

<section class="filters">
  <div class="filter-half seekers">
    <div class="filter-col"><h4>OCCUP. GROUPS</h4><ul><li>Students</li><li>Young Workers</li><li>Full-time Workers</li></ul></div>
    <div class="filter-col"><h4>AGE GROUPS</h4><ul><li>Under 20 YO</li><li>20 YO – 30 YO</li><li>Over 30 YO</li></ul></div>
    <div class="filter-col"><h4>GENDER GROUPS</h4><ul><li>Men &amp; Women</li><li>Men only</li><li>Women only</li></ul></div>
  </div>
  <div class="filter-half owners">
    <div class="filter-col"><h4>CITIES</h4><ul><li>London</li><li>Paris</li><li>Brussels</li></ul></div>
    <div class="filter-col"><h4>RENT</h4><ul><li>Under €350</li><li>€350 – €600</li><li>Over €600</li></ul></div>
    <div class="filter-col"><h4>AVAILABILITY</h4><ul><li>Now</li><li>In a month</li><li>In 3 months</li></ul></div>
  </div>
</section>

<footer class="site-footer">
  <div class="foot-col"><h4>INFORMATION</h4><ul><li>Home</li><li>About Us</li><li>FAQs</li><li>Contact Us</li><li>Terms and Conditions</li></ul></div>
  <div class="foot-col"><h4>GROUPS</h4><ul><li>Look for a group</li><li>Join a group</li><li>Create a group</li></ul></div>
  <div class="foot-col"><h4>PROPERTIES</h4><ul><li>Look for a house / appartement</li><li>Apply</li><li>Why flatshare?</li><li>Sales Conditions</li><li>Advertise</li></ul></div>
  <div class="foot-col"><h4>CONTACT US</h4>
    <div class="contact-line">info@lanternnestplace.com</div>
    <div class="contact-line">+32 9 876 54 32</div>
    <div class="social"><span></span><span></span><span></span></div>
    <div class="copyright">©2016 Lantern Nest Place.</div>
  </div>
</footer>

</body>
</html>
```